" atendimento de pacientes de ambos os gêneros com uma ênfase em mulheres, oferecemos cirurgia plástica estética e reparadora . local de requinte e sofisticação "

```html
<!DOCTYPE html>
<html lang="pt-BR">
<head>
<meta charset="utf-8">
<title>Velaris Cirurgia Plástica – Cartão</title>
<link rel="stylesheet" href="https://fonts.googleapis.com/css2?family=Cinzel:wght@400;500&family=Montserrat:wght@400;500&display=swap">
<style>
  :root {
    --bg-center: #2c2c2c;
    --bg-edge: #161616;
    --disc-center: #3a3a3a;
    --disc-edge: #141414;
    --gold-light: #f3d27a;
    --gold: #d4a33a;
    --gold-deep: #9c6d1c;
    --ring-white: #f4f1ea;
    --text-light: #f2f2f2;
    --icon-ink: #1c1c1c;
  }
  * { margin: 0; padding: 0; box-sizing: border-box; }
  html, body { width: 1200px; height: 1200px; overflow: hidden; }
  body {
    background: var(--bg-edge);
    font-family: "Montserrat", Arial, sans-serif;
  }
  .card {
    position: relative;
    width: 1200px;
    height: 1200px;
    background: radial-gradient(circle at 50% 50%, var(--bg-center), var(--bg-edge) 80%);
    overflow: hidden;
  }
  .badge {
    position: absolute;
    left: 160px;
    top: 192px;
    width: 886px;
    height: 886px;
    border-radius: 50%;
    background: linear-gradient(150deg, var(--gold-light), var(--gold) 35%, var(--gold-deep) 70%, var(--gold-light));
    box-shadow: 0 20px 50px rgba(0,0,0,.6);
  }
  .badge-white-ring {
    position: absolute;
    inset: 13px;
    border-radius: 50%;
    background: var(--ring-white);
  }
  .badge-inner-gold {
    position: absolute;
    inset: 26px;
    border-radius: 50%;
    background: linear-gradient(330deg, var(--gold-light), var(--gold) 40%, var(--gold-deep));
  }
  .badge-disc {
    position: absolute;
    inset: 33px;
    border-radius: 50%;
    background: radial-gradient(circle at 45% 40%, var(--disc-center), var(--disc-edge) 75%);
  }
  .badge-content {
    position: absolute;
    inset: 0;
    text-align: center;
  }
  .brand-dot {
    position: absolute;
    left: 50%;
    top: 82px;
    width: 100px;
    height: 100px;
    margin-left: -50px;
    border-radius: 50%;
    background: var(--gold);
  }
  .brand-name {
    position: absolute;
    left: 0; right: 0;
    top: 252px;
    font-family: "Cinzel", Georgia, serif;
    font-weight: 400;
    font-size: 86px;
    line-height: 1;
    letter-spacing: 5px;
    color: var(--gold);
  }
  .brand-tagline {
    position: absolute;
    left: 0; right: 0;
    top: 350px;
    font-family: "Cinzel", Georgia, serif;
    font-size: 22px;
    line-height: 1;
    letter-spacing: 5px;
    color: var(--gold);
  }
  .contact-row {
    position: absolute;
    left: 0; right: 0;
    display: flex;
    justify-content: center;
    align-items: center;
    gap: 16px;
    color: var(--text-light);
    font-size: 31px;
    line-height: 1;
  }
  .contact-phone { top: 468px; }
  .contact-web { top: 554px; }
  .contact-icon {
    width: 46px;
    height: 46px;
    border-radius: 50%;
    background: var(--gold);
    display: flex;
    align-items: center;
    justify-content: center;
  }
  .social-marks {
    position: absolute;
    left: 0; right: 0;
    top: 678px;
    display: flex;
    justify-content: center;
    gap: 7px;
  }
  .social-marks span {
    width: 34px;
    height: 34px;
    border-radius: 4px;
    background: var(--gold);
  }
  .social-handle {
    position: absolute;
    left: 0; right: 0;
    top: 722px;
    color: var(--text-light);
    font-size: 25px;
    line-height: 1;
  }
</style>
</head>
<body>
<main class="card">
  <section class="badge">
    <div class="badge-white-ring"></div>
    <div class="badge-inner-gold"></div>
    <div class="badge-disc"></div>
    <div class="badge-content">
      <div class="brand-dot"></div>
      <h1 class="brand-name">VELARIS</h1>
      <p class="brand-tagline">CIRURGIA PLÁSTICA</p>

      <div class="contact-row contact-phone">
        <span class="contact-icon">
          <svg width="26" height="26" viewBox="0 0 24 24" fill="var(--icon-ink)">
            <path d="M6.6 10.8a15.1 15.1 0 0 0 6.6 6.6l2.2-2.2a1 1 0 0 1 1-.25 11.4 11.4 0 0 0 3.6.57 1 1 0 0 1 1 1V20a1 1 0 0 1-1 1A17 17 0 0 1 3 4a1 1 0 0 1 1-1h3.5a1 1 0 0 1 1 1c0 1.25.2 2.45.57 3.57a1 1 0 0 1-.25 1z"/>
          </svg>
        </span>
        <span>(xx) xxxx-xxxx</span>
      </div>

      <div class="contact-row contact-web">
        <span class="contact-icon">
          <svg width="28" height="28" viewBox="0 0 30 30" fill="none" stroke="var(--icon-ink)" stroke-width="2">
            <circle cx="15" cy="15" r="11"/>
            <ellipse cx="15" cy="15" rx="5" ry="11"/>
            <line x1="4" y1="15" x2="26" y2="15"/>
            <line x1="6" y1="9" x2="24" y2="9"/>
            <line x1="6" y1="21" x2="24" y2="21"/>
          </svg>
        </span>
        <span>www.suaclinica.com</span>
      </div>

      <div class="social-marks"><span></span><span></span><span></span></div>
      <p class="social-handle">/Velaris</p>
    </div>
  </section>
</main>
</body>
</html>
```